Modernization of existing web site

Update existing web site to a professional look vs a home-made site. Site look and navigation should be up to today's standards and display properly on mobile devices.
Only simple HTML and CSS is to be used as this is a basic site. No content management.
Existing site is https://www.plexumar.example

Target Market(s)

Insurance and Technology

Industry/Entity Type

Insurance and technology

Coding

Coded - Design and coding required

Number of Pages Required

5+ page

Font styles to use
Sans Serif

Colors
0054AA
0677BA
7BADD7
CADEEF
E8F1F8
0094D4
00A9DD
6FCCEA
C7EBF8
E9F6FB

Requirements
Must have
• A sleek, modern feel and also done with a button-downed industry in mind.
Nice to have
• Clean integration of the logo and name
Should not have
• Open to ideas

```html
<!DOCTYPE html>
<html lang="en">
<head>
<meta charset="utf-8">
<title>Plexumar — Navigating business and technology</title>
<link href="https://fonts.googleapis.com/css2?family=Montserrat:wght@400;500;600;700&display=swap" rel="stylesheet">
<style>
:root{
  --navy:#0b1a36;
  --blue-deep:#0054AA;
  --blue:#0677BA;
  --blue-mid:#7BADD7;
  --blue-pale:#CADEEF;
  --blue-wash:#E2ECF8;
  --cyan:#0094D4;
  --cyan-bright:#00A9DD;
  --cyan-soft:#6FCCEA;
  --ink:#111827;
  --grey:#5b6270;
  --white:#ffffff;
}
*{margin:0;padding:0;box-sizing:border-box}
html,body{width:1200px;height:3366px;overflow:hidden}
body{font-family:'Montserrat',sans-serif;color:var(--ink);background:var(--white);position:relative}
.abs{position:absolute}
a{color:inherit;text-decoration:none}

/* Hero */
.hero{left:0;top:0;width:1200px;height:712px;background:radial-gradient(ellipse at 70% 40%,#1d4f9a 0%,#10295a 40%,var(--navy) 75%);overflow:hidden}
.hero-curve{left:0;top:470px;width:1200px;height:250px}
.hero-visual{left:560px;top:150px;width:480px;height:430px;border-radius:50%;background:radial-gradient(circle at 50% 42%,#bfe8ff 0%,#3aa0e6 12%,#1f5fb0 35%,rgba(16,41,90,0) 70%)}
.brand{display:flex;align-items:center;gap:12px;font-weight:700;letter-spacing:.5px}
.brand-dot{border-radius:50%;display:block}
.hero .brand{left:111px;top:26px;font-size:44px;color:var(--white)}
.hero .brand-dot{width:52px;height:52px;border:5px solid var(--white)}
.topbar{right:111px;top:20px;font-size:16px;color:#dfe6f3;display:flex;gap:14px;align-items:center}
.topbar svg{vertical-align:-2px;margin-right:4px}
.nav{right:111px;top:66px;display:flex;gap:30px;font-size:18px;font-weight:600;color:var(--white)}
.nav .active{color:var(--cyan-bright)}
.hero h1{left:111px;top:148px;width:520px;font-size:44px;line-height:51px;font-weight:700;color:var(--white)}
.hero-lead{left:111px;top:328px;width:430px;font-size:21px;line-height:32px;color:var(--white)}
.btn{display:inline-block;background:var(--cyan-bright);color:var(--white);font-weight:600;border-radius:40px;text-align:center;text-transform:uppercase}
.hero .btn{left:111px;top:426px;width:222px;height:65px;line-height:65px;font-size:19px}

/* Welcome */
.welcome-visual{left:20px;top:725px;width:516px;height:472px;border-radius:50%;background:linear-gradient(135deg,#e9f6fb 0%,#9fd3ef 40%,#0094D4 65%,#0054AA 100%)}
.section-title{font-size:40px;font-weight:700;letter-spacing:.5px;color:var(--ink);text-transform:uppercase}
.section-title span{color:var(--blue-deep)}
.welcome .section-title{left:586px;top:798px}
.body-copy{font-size:17px;line-height:26.5px;color:var(--grey)}
.welcome .body-copy{left:586px;top:870px;width:510px}
.body-copy p+p{margin-top:27px}
.welcome .btn{left:586px;top:1089px;width:166px;height:57px;line-height:57px;font-size:18px}

/* Services */
.services{left:0;top:1259px;width:1200px;height:607px;background:linear-gradient(180deg,#e3edf9 0%,#d8e6f5 100%);overflow:hidden}
.services .section-title{left:111px;top:64px}
.services-visual{left:680px;top:40px;width:720px;height:720px;border-radius:50%;background:linear-gradient(160deg,#1a3d6e 0%,#2a5b8c 35%,#0e7ea8 65%,#00e0f0 100%)}
.svc{display:flex;align-items:center;gap:12px;font-size:18px;line-height:23px;color:var(--ink);font-weight:500;width:290px}
.svc-icon{flex:0 0 57px;width:57px;height:57px;border-radius:50%;background:var(--white);display:flex;align-items:center;justify-content:center;box-shadow:0 1px 3px rgba(0,40,90,.12)}

/* About */
.about-visual{left:0;top:1880px;width:399px;height:444px;border-radius:0 260px 0 0;background:linear-gradient(180deg,#f2f2f2 0%,#d6d6d6 55%,#222 56%,#111 100%)}
.about .section-title{left:505px;top:1934px}
.about .body-copy{left:505px;top:2006px;width:590px}
.about .btn{left:505px;top:2202px;width:166px;height:57px;line-height:57px;font-size:18px}

/* Contact */
.help{left:0;top:2324px;width:1200px;height:653px;background:linear-gradient(90deg,#0054AA 0%,#0054AA 45%,#1c5fb3 70%,#2d6fc0 100%);overflow:hidden}
.help-visual{left:640px;top:80px;width:620px;height:620px;border-radius:50%;background:radial-gradient(circle,#9cc8f0 0%,#3f80cf 30%,rgba(0,84,170,0) 70%)}
.help h2{left:112px;top:54px;font-size:40px;font-weight:700;color:var(--white);text-transform:uppercase}
.help-lead{left:112px;top:130px;width:490px;font-size:17px;line-height:26px;color:var(--white)}
.field{background:var(--white);border-radius:3px;font-size:17px;color:#555;padding:0 17px;display:flex;align-items:center}
.field.area{align-items:flex-start;padding-top:17px}
.help .btn{left:112px;top:538px;width:128px;height:55px;line-height:55px;font-size:18px}

/* Footer */
.footer .brand{left:111px;top:3100px;font-size:58px;color:var(--blue-deep)}
.footer .brand-dot{width:70px;height:70px;background:var(--blue-deep)}
.foot-head{font-size:19px;font-weight:600;color:var(--ink)}
.foot-list{list-style:none;font-size:16px;color:var(--grey)}
.foot-list li{height:30.3px}
.contact-list{list-style:none;font-size:16px;color:var(--grey)}
.contact-list li{display:flex;align-items:center;gap:8px;position:absolute;left:0;white-space:nowrap}
.rule{left:111px;top:3273px;width:978px;height:2px;background:#cfd3d9}
.copyright{left:111px;top:3305px;font-size:16px;color:var(--grey)}
.social{left:960px;top:3297px;display:flex;gap:6px}
.social span{width:38px;height:38px;border-radius:50%;border:1.5px solid var(--blue-mid);display:flex;align-items:center;justify-content:center}
.social span i{width:10px;height:10px;border-radius:50%;background:var(--blue)}
</style>
</head>
<body>

<header class="hero abs">
  <div class="hero-visual abs" role="img" aria-label="Glowing digital globe with world map and radar arcs"></div>
  <svg class="hero-curve abs" viewBox="0 0 1200 250" preserveAspectRatio="none" aria-hidden="true">
    <path d="M0 14 C60 120 160 180 320 200 C600 232 900 230 1200 236 L1200 250 L0 250 Z" fill="#ffffff"/>
  </svg>
  <div class="brand abs"><span class="brand-dot"></span>PLEXUMAR</div>
  <div class="topbar abs">
    <span><svg width="14" height="14" viewBox="0 0 24 24"><path fill="#dfe6f3" d="M6.6 10.8c1.4 2.8 3.8 5.1 6.6 6.6l2.2-2.2c.3-.3.7-.4 1-.2 1.1.4 2.3.6 3.6.6.6 0 1 .4 1 1V20c0 .6-.4 1-1 1C10.6 21 3 13.4 3 4c0-.6.4-1 1-1h3.5c.6 0 1 .4 1 1 0 1.3.2 2.5.6 3.6.1.3 0 .7-.2 1z"/></svg>555-014-2290</span>
    <span>|</span>
    <span><svg width="15" height="13" viewBox="0 0 24 20"><rect x="1" y="2" width="22" height="16" rx="2" fill="#dfe6f3"/><path d="M2 3l10 8 10-8" stroke="#10295a" stroke-width="2" fill="none"/></svg>info@plexumar.example</span>
  </div>
  <nav class="nav abs">
    <a class="active" href="#">Home</a><a href="#">Services</a><a href="#">About Us</a><a href="#">Contact Us</a>
  </nav>
  <h1 class="abs">Navigating business and technology to generate results</h1>
  <p class="hero-lead abs">we are here to assist you in realizing your vision for your business.</p>
  <a class="btn abs" href="#">Get More Info</a>
</header>

<section class="welcome">
  <div class="welcome-visual abs" role="img" aria-label="Hands holding a tablet showing business charts"></div>
  <h2 class="section-title abs">Welcome to <span>Plexumar</span></h2>
  <div class="body-copy abs">
    <p>We offer a number of different services for insurance, technology, and financial services firms.</p>
    <p>We have extensive experience in many areas of business and technology combined with a deep level of integrity in the way we do business. If you have a specific need not mentioned on our website, contact us today with your details.</p>
  </div>
  <a class="btn abs" href="#">Read More</a>
</section>

<section class="services abs">
  <div class="services-visual abs" role="img" aria-label="Hands typing on a keyboard with glowing financial bar and line charts"></div>
  <h2 class="section-title abs">Our <span>Services</span></h2>

  <div class="svc abs" style="left:111px;top:145px"><span class="svc-icon"><svg width="24" height="28" viewBox="0 0 24 28"><circle cx="12" cy="10" r="7" fill="none" stroke="#0677BA" stroke-width="2.2"/><rect x="8" y="19" width="8" height="5" rx="1" fill="#0677BA"/></svg></span>Business and Technology Strategy</div>
  <div class="svc abs" style="left:111px;top:213px"><span class="svc-icon"><svg width="30" height="26" viewBox="0 0 30 26"><rect x="2" y="2" width="26" height="16" rx="2" fill="#0677BA"/><rect x="5" y="5" width="20" height="10" fill="#fff"/><rect x="11" y="19" width="8" height="3" fill="#0677BA"/><rect x="8" y="22" width="14" height="2" fill="#0677BA"/></svg></span>Technology Implementation</div>
  <div class="svc abs" style="left:111px;top:285px"><span class="svc-icon"><svg width="26" height="26" viewBox="0 0 26 26"><circle cx="13" cy="13" r="11" fill="#0677BA"/><path d="M7 9c3 0 4 2 3 4s2 3 1 6M15 5c0 3 4 3 5 6" stroke="#fff" stroke-width="2" fill="none"/></svg></span>Distribution Channel Development</div>
  <div class="svc abs" style="left:111px;top:357px"><span class="svc-icon"><svg width="34" height="30" viewBox="0 0 34 30"><circle cx="12" cy="17" r="8" fill="none" stroke="#0677BA" stroke-width="4" stroke-dasharray="3 2.3"/><circle cx="12" cy="17" r="3" fill="#0677BA"/><circle cx="26" cy="8" r="5" fill="none" stroke="#0677BA" stroke-width="3" stroke-dasharray="2 1.8"/></svg></span>Product Development</div>
  <div class="svc abs" style="left:111px;top:425px"><span class="svc-icon"><svg width="28" height="28" viewBox="0 0 24 24"><path fill="#0677BA" d="M12 2l3 6.5 7 .8-5.2 4.8 1.4 7L12 17.6 5.8 21.1l1.4-7L2 9.3l7-.8z"/></svg></span>Rating and Regulatory</div>
  <div class="svc abs" style="left:111px;top:495px"><span class="svc-icon"><svg width="28" height="28" viewBox="0 0 28 28"><path d="M2 14A12 12 0 0 1 26 14Z" fill="#0677BA"/><path d="M14 14v8a3 3 0 0 1-6 0" stroke="#0677BA" stroke-width="2" fill="none"/></svg></span>Reinsurance</div>

  <div class="svc abs" style="left:408px;top:145px"><span class="svc-icon"><svg width="28" height="26" viewBox="0 0 28 26"><path d="M14 2L27 24H1z" fill="#0677BA"/><rect x="12.8" y="9" width="2.4" height="8" fill="#fff"/><rect x="12.8" y="19" width="2.4" height="2.4" fill="#fff"/></svg></span>Catastrophe Risk Management</div>
  <div class="svc abs" style="left:408px;top:213px"><span class="svc-icon"><svg width="26" height="26" viewBox="0 0 26 26"><circle cx="11" cy="11" r="7" fill="none" stroke="#0677BA" stroke-width="3"/><path d="M16 16l7 7" stroke="#0677BA" stroke-width="3.5" stroke-linecap="round"/></svg></span>M &amp; A Due Diligence</div>
  <div class="svc abs" style="left:408px;top:285px"><span class="svc-icon"><svg width="26" height="26" viewBox="0 0 26 26"><circle cx="13" cy="13" r="8" fill="none" stroke="#0677BA" stroke-width="5" stroke-dasharray="3.2 3"/><circle cx="13" cy="13" r="6" fill="#0677BA"/><circle cx="13" cy="13" r="2.5" fill="#fff"/></svg></span>Enterprise Risk Management</div>
  <div class="svc abs" style="left:408px;top:357px"><span class="svc-icon"><svg width="30" height="26" viewBox="0 0 30 26"><path d="M2 2v22h26" stroke="#0677BA" stroke-width="2" fill="none"/><rect x="7" y="12" width="3" height="10" fill="#0677BA"/><rect x="12" y="8" width="3" height="14" fill="#0677BA"/><rect x="17" y="14" width="3" height="8" fill="#0677BA"/><rect x="22" y="6" width="3" height="16" fill="#0677BA"/></svg></span>Data/Reporting/ Analytics</div>
  <div class="svc abs" style="left:408px;top:425px"><span class="svc-icon"><svg width="34" height="26" viewBox="0 0 34 26"><circle cx="8" cy="8" r="4" fill="#0677BA"/><circle cx="26" cy="8" r="4" fill="#0677BA"/><circle cx="17" cy="7" r="5" fill="#0677BA"/><path d="M1 20a7 6 0 0 1 12 0zM21 20a7 6 0 0 1 12 0z" fill="#0677BA"/><path d="M8 24a9 8 0 0 1 18 0z" fill="#0677BA"/></svg></span>Interim Executive Leadership</div>
</section>

<section class="about">
  <div class="about-visual abs" role="img" aria-label="Portrait photo of the firm's founder in a dark suit"></div>
  <h2 class="section-title abs">About <span>Plexumar</span></h2>
  <div class="body-copy abs">
    <p>Plexumar was formed in late 2018 to bring over 35 years of experience in multiple industries and disciplines to our customers.</p>
    <p>Dan Mercer has led large and small organizations.&nbsp; With senior executive experience in business and technology, he has a distinct view of the business and technology needs of organizations.</p>
  </div>
  <a class="btn abs" href="#">Read More</a>
</section>

<section class="help abs">
  <div class="help-visual abs" role="img" aria-label="Digital compass over a blue data background"></div>
  <h2 class="abs">We’re here to help</h2>
  <p class="help-lead abs">If you have any questions or requests about our company or the services we provide, please call or email us, or use the form below.</p>
  <div class="field abs" style="left:112px;top:221px;width:282px;height:53px">First Name*</div>
  <div class="field abs" style="left:403px;top:221px;width:282px;height:53px">Last Name*</div>
  <div class="field abs" style="left:112px;top:283px;width:282px;height:53px">Company*</div>
  <div class="field abs" style="left:403px;top:283px;width:282px;height:53px">Email*</div>
  <div class="field abs" style="left:112px;top:344px;width:573px;height:53px">Subject</div>
  <div class="field area abs" style="left:112px;top:404px;width:573px;height:111px">How can we help you? *</div>
  <a class="btn abs" href="#">Submit</a>
</section>

<footer class="footer">
  <div class="brand abs"><span class="brand-dot"></span>PLEXUMAR</div>
  <div class="abs" style="left:559px;top:3046px">
    <h3 class="foot-head">Quick Links</h3>
    <ul class="foot-list" style="margin-top:14px">
      <li>Home</li><li>Our Services</li><li>About Us</li><li>Contact Us</li><li>Privacy Policy</li>
    </ul>
  </div>
  <div class="abs" style="left:747px;top:3046px;width:360px;height:180px">
    <h3 class="foot-head">Contact Us</h3>
    <ul class="contact-list">
      <li style="top:46px"><svg width="11" height="15" viewBox="0 0 12 16"><path d="M6 0a6 6 0 0 1 6 6c0 4.5-6 10-6 10S0 10.5 0 6a6 6 0 0 1 6-6z" fill="#0677BA"/><circle cx="6" cy="6" r="2.2" fill="#fff"/></svg>42 Harbor Ridge Ln&nbsp; Reno, NV 89501</li>
      <li style="top:106px"><svg width="14" height="14" viewBox="0 0 24 24"><path fill="#0677BA" d="M6.6 10.8c1.4 2.8 3.8 5.1 6.6 6.6l2.2-2.2c.3-.3.7-.4 1-.2 1.1.4 2.3.6 3.6.6.6 0 1 .4 1 1V20c0 .6-.4 1-1 1C10.6 21 3 13.4 3 4c0-.6.4-1 1-1h3.5c.6 0 1 .4 1 1 0 1.3.2 2.5.6 3.6.1.3 0 .7-.2 1z"/></svg>555-014-2290</li>
      <li style="top:166px"><svg width="16" height="13" viewBox="0 0 24 20"><rect x="1" y="2" width="22" height="16" rx="2" fill="#0677BA"/><path d="M2 3l10 8 10-8" stroke="#fff" stroke-width="2" fill="none"/></svg>info@plexumar.example</li>
    </ul>
  </div>
  <div class="rule abs"></div>
  <p class="copyright abs">© 2022, Plexumar. All rights reserved.</p>
  <div class="social abs" aria-label="Social links"><span><i></i></span><span><i></i></span><span><i></i></span></div>
</footer>

</body>
</html>
```